Ceiling fan flyer design

We are after a double sided flyer design offering ceiling fan installations

Target Market(s)

Home owners

Requirements
Must have
• content listed

```html
<!DOCTYPE html>
<html lang="en">
<head>
<meta charset="utf-8">
<title>Ceiling Fan Flyer – Call A Sparky</title>
<link rel="stylesheet" href="https://fonts.googleapis.com/css2?family=Anton&family=Oswald:wght@500;600&family=Archivo+Narrow:wght@500;700&family=Tinos:wght@400;700&display=swap">
<style>
  :root {
    --ink: #111111;
    --navy: #1a2a5c;
    --red: #d8181c;
    --offer-red: #c41414;
    --white: #ffffff;
    --panel-dark: rgba(40, 40, 46, 0.9);
    --bar-dark: #141414;
    --hero-green: #4c9a3a;
    --hero-cape: #d7452a;
    --brand-orange: #e4792a;
    --card-blue: #1d3f8f;
    --card-red: #b8242a;
    --card-teal: #3b8fc4;
  }
  * { box-sizing: border-box; margin: 0; padding: 0; }
  html, body { width: 1200px; height: 717px; overflow: hidden; background: var(--white); }
  .canvas { position: relative; width: 1200px; height: 717px; background: var(--white); }

  /* ---------- Front side ---------- */
  .front {
    position: absolute; left: 0; top: 0; width: 502px; height: 717px; overflow: hidden;
    border: 2px solid var(--ink);
    background:
      radial-gradient(ellipse at 50% 8%, rgba(255,255,255,0.95) 0%, rgba(255,255,255,0.75) 28%, rgba(255,255,255,0) 55%),
      linear-gradient(135deg, #f6a23a 0%, #f07bb0 30%, #b6e07a 55%, #f4d24a 75%, #ea6aa8 100%);
  }
  .front__headline {
    position: absolute; top: 8px; left: 0; width: 100%; text-align: center;
    font-family: "Oswald", sans-serif; font-weight: 500; font-size: 37px; color: var(--ink); letter-spacing: 0.5px;
  }
  .front__subhead {
    position: absolute; top: 56px; left: 0; width: 100%; text-align: center;
    font-family: "Archivo Narrow", sans-serif; font-weight: 500; font-size: 36px; color: var(--navy);
  }
  .front__intro {
    position: absolute; top: 104px; left: 16px; width: 480px;
    font-family: "Archivo Narrow", sans-serif; font-weight: 500; font-size: 22.5px; line-height: 30px; color: var(--navy);
  }
  .hero-illustration {
    position: absolute; left: 120px; top: 176px; width: 350px; height: 300px; border-radius: 46% 46% 30% 30%;
    background: radial-gradient(ellipse at 50% 40%, var(--hero-green) 0%, #6fb34c 45%, var(--hero-cape) 100%);
    opacity: 0.85;
  }
  .testimonial { position: absolute; left: 12px; width: 220px; font-family: "Tinos", serif; color: var(--ink); }
  .testimonial--one { top: 180px; }
  .testimonial--two { top: 260px; }
  .testimonial__lead { font-weight: 700; font-size: 17px; color: var(--red); }
  .testimonial__body { font-size: 14px; line-height: 17px; }
  .testimonial__name { font-size: 14px; color: var(--red); margin-top: 4px; }

  .offer {
    position: absolute; left: 352px; top: 424px; width: 146px; text-align: center;
    font-family: "Tinos", serif; color: var(--offer-red);
  }
  .offer__amount { font-family: "Archivo Narrow", sans-serif; font-weight: 700; font-size: 22px; }
  .offer__detail { font-size: 17px; line-height: 20px; }

  .brand {
    position: absolute; left: 14px; top: 488px; width: 330px;
    font-family: "Anton", sans-serif; font-size: 46px; line-height: 52px; color: var(--brand-orange); text-transform: uppercase;
    display: flex; align-items: flex-start; gap: 10px;
  }
  .brand__mark { flex: none; width: 26px; height: 26px; border-radius: 50%; background: var(--brand-orange); margin-top: 14px; }

  .conditions {
    position: absolute; left: 0; bottom: 0; width: 100%; height: 74px; background: var(--bar-dark);
    padding: 8px 10px; font-family: "Tinos", serif; color: var(--red);
  }
  .conditions__title { font-family: "Archivo Narrow", sans-serif; font-size: 21px; }
  .conditions__text { font-size: 15.5px; line-height: 18px; }

  /* ---------- Back side ---------- */
  .back {
    position: absolute; left: 639px; top: 0; width: 530px; height: 713px; overflow: hidden;
    border: 1px solid #cccccc;
    background:
      linear-gradient(180deg, rgba(255,255,255,1) 0%, rgba(255,255,255,0.96) 38%, rgba(255,255,255,0) 60%),
      conic-gradient(from 0deg at 50% 62%, #f44a4a, #f7a53a, #f4ea48, #6fd36a, #42c7e6, #5b6ff0, #c05ae8, #f45aa8, #f44a4a);
  }
  .back__title {
    position: absolute; top: 44px; left: 0; width: 100%; text-align: center;
    font-family: "Anton", sans-serif; font-size: 44px; color: var(--ink);
  }
  .guarantees {
    position: absolute; top: 112px; left: 14px; width: 505px; list-style: none;
    font-family: "Tinos", serif; font-size: 16.5px; line-height: 26px; color: var(--ink);
  }
  .contact-panel {
    position: absolute; left: 18px; top: 386px; width: 494px; height: 284px;
    background: var(--panel-dark); border-radius: 10px; padding: 28px 18px; color: var(--white);
  }
  .contact-panel__details { font-family: "Archivo Narrow", sans-serif; font-size: 17px; line-height: 22px; }
  .contact-panel__label { font-weight: 700; }
  .contact-panel__cards-label { margin-top: 44px; font-family: "Archivo Narrow", sans-serif; font-size: 17px; }
  .payment-list { display: flex; gap: 6px; margin-top: 14px; }
  .payment-card {
    width: 86px; height: 50px; background: var(--white); display: flex; align-items: center; justify-content: center;
    font-family: "Archivo Narrow", sans-serif; font-weight: 700; font-size: 15px;
  }
  .payment-card--one { color: var(--card-blue); }
  .payment-card--two { color: var(--card-red); }
  .payment-card--three { color: var(--card-teal); }
</style>
</head>
<body>
<main class="canvas">

  <section class="front">
    <h1 class="front__headline">HOT SWEATY UNCOMFORTABLE</h1>
    <h2 class="front__subhead">A breeze without the cost!</h2>
    <p class="front__intro">Enjoy the gentle breeze &amp; cooling effect of a ceiling fan to help you sleep soundly at night &amp; be more productive</p>

    <div class="hero-illustration" role="img" aria-label="Cartoon electrician superhero in green suit and red cape giving a thumbs up and holding a cable"></div>

    <blockquote class="testimonial testimonial--one">
      <p class="testimonial__lead">We can now sleep! <span class="testimonial__body" style="color:var(--ink);font-weight:400">Wow what a difference!</span></p>
      <p class="testimonial__body">Thanks Marcus for your help."</p>
      <p class="testimonial__name">-Graham &amp; Lucy Pemberton</p>
    </blockquote>

    <blockquote class="testimonial testimonial--two">
      <p class="testimonial__lead">“Super service!</p>
      <p class="testimonial__body">What a pleasant change.<br>Marcus could not have done more to ensure our satisfaction."</p>
      <p class="testimonial__name">-Tom &amp; Rosa Delvecchio</p>
    </blockquote>

    <div class="offer">
      <p class="offer__amount">Save $25 OFF</p>
      <p class="offer__detail">for every<br>2nd fan installed</p>
    </div>

    <div class="brand"><span class="brand__mark"></span><span>Call A Sparky Pty Ltd</span></div>

    <footer class="conditions">
      <p class="conditions__text"><span class="conditions__title">Conditions:</span> Mention this ad when booking to receive offer.<br>Limit one per household. Cannot be combined with any other offer</p>
    </footer>
  </section>

  <section class="back">
    <h2 class="back__title">We guarantee to -</h2>
    <ul class="guarantees">
      <li>- Always be on time, or we pay you $100</li>
      <li>- Tell you the exact cost before any job begins</li>
      <li>- Provide you with a fixed price guarantee, assuring you have no extra costs</li>
      <li>- Leave your place as clean as it was when we first arrived</li>
      <li>- Return, and fix it for free, if its not right</li>
      <li>- Return your telephone calls promptly</li>
      <li>- Provide a minimum 12 Month warranty on all parts</li>
      <li>- Provide friendly, helpful service and advice</li>
    </ul>

    <div class="contact-panel">
      <p class="contact-panel__details"><span class="contact-panel__label">Contact Details:</span> 1300 482 615<br>www.callasparky.com.au<br>lic no: 415962K</p>
      <p class="contact-panel__cards-label">We accept all major credit card:</p>
      <div class="payment-list">
        <span class="payment-card payment-card--one">VERITAS</span>
        <span class="payment-card payment-card--two">CoinCard</span>
        <span class="payment-card payment-card--three">AURUM</span>
      </div>
    </div>
  </section>

</main>
</body>
</html>
```